Flyer/Poster Tischtennis Sportverein
Zielgruppe
Tischtennisverein - Zielgruppe: Kinder von 8 - 12 Jahren
Aufgabenstellung
Allgemeiner Flyer für Tischtennisverein - Werbung für Kindertraining, Texbereich sollte im Design enthalten sein, aber so gestaltet dass der Text je nach Bedarf durch uns angepasst werden kann
DIN Format: Sollte als Postkartenformat sowie als DIN A3 oder DIN A2 Poster zu verwenden
Angehängtes Logo einbinden aber nicht zu prominent

```html
<!DOCTYPE html>
<html lang="de">
<head>
<meta charset="utf-8">
<title>Kindertraining Flyer</title>
<link rel="stylesheet" href="https://fonts.googleapis.com/css2?family=Patrick+Hand&family=Open+Sans:wght@400;700&display=swap">
<style>
  :root {
    --stage: #f2f2f2;
    --sky: #8fcad8;
    --sky-deep: #7bbbd0;
    --edge-blue: #1b6db3;
    --card: #f4f4f4;
    --ink: #3a3a3a;
    --red: #d6134f;
    --magenta: #b5268f;
    --teal: #1a9fb5;
    --lilac: #9a8fd0;
    --lime: #9cc43a;
    --paddle: #d4084f;
    --paddle-light: #e2356c;
    --grip: #b9b9b9;
  }
  * { box-sizing: border-box; margin: 0; padding: 0; }
  html, body { width: 1200px; height: 720px; overflow: hidden; }
  body { background: var(--stage); position: relative; }

  .flyer {
    position: absolute;
    left: 360px; top: 20px;
    width: 480px; height: 680px;
    overflow: hidden;
    background:
      radial-gradient(ellipse at 55% 55%, var(--sky) 0%, var(--sky) 45%, var(--sky-deep) 70%, var(--edge-blue) 100%);
    box-shadow: 0 10px 30px rgba(0,0,0,0.15);
  }
  .flyer__texture {
    position: absolute; inset: 0;
    background:
      linear-gradient(90deg, rgba(27,109,179,0.75) 0%, rgba(27,109,179,0) 12%),
      linear-gradient(180deg, rgba(27,109,179,0.7) 0%, rgba(27,109,179,0) 10%),
      linear-gradient(0deg, rgba(27,109,179,0.55) 0%, rgba(27,109,179,0) 8%);
  }

  .badge {
    position: absolute;
    left: 50%; top: 72px;
    width: 360px; height: 360px;
    transform: translateX(-50%);
    filter: drop-shadow(0 4px 8px rgba(0,0,0,0.18));
  }
  .badge svg { position: absolute; inset: 0; }
  .badge__content {
    position: absolute; inset: 0;
    display: flex; flex-direction: column; align-items: center;
    padding: 54px 46px 0;
    text-align: center;
  }
  .badge__title {
    font-family: "Patrick Hand", cursive;
    font-weight: 400;
    font-size: 38px;
    letter-spacing: 2px;
    line-height: 1;
    background: linear-gradient(90deg, var(--red), var(--magenta) 30%, var(--lilac) 60%, var(--lime));
    -webkit-background-clip: text;
    background-clip: text;
    color: transparent;
  }
  .badge__body {
    margin-top: 12px;
    font-family: "Open Sans", sans-serif;
    font-size: 10.5px;
    line-height: 1.45;
    color: var(--ink);
  }
  .badge__dates {
    margin-top: 8px;
    font-family: "Open Sans", sans-serif;
    font-weight: 700;
    font-size: 11px;
    line-height: 1.35;
  }
  .date--wed { color: var(--red); }
  .date--thu { color: var(--magenta); }
  .date--fri { color: var(--teal); }
  .badge__club {
    margin-top: 14px;
    display: flex; align-items: center; gap: 5px;
    font-family: "Open Sans", sans-serif;
    font-weight: 700;
    font-size: 10px;
    color: var(--red);
  }
  .badge__club-dot {
    width: 12px; height: 12px; border-radius: 50%;
    background: var(--red);
  }

  .paddles {
    position: absolute;
    left: 120px; top: 450px;
    width: 220px; height: 150px;
    border-radius: 16px;
    background: linear-gradient(150deg, var(--paddle) 0%, var(--paddle-light) 55%, var(--grip) 100%);
  }

  .flyer__url {
    position: absolute;
    left: 0; right: 0; bottom: 28px;
    text-align: center;
    font-family: "Patrick Hand", cursive;
    font-size: 26px;
    letter-spacing: 2px;
    color: #ffffff;
  }
</style>
</head>
<body>
  <main class="flyer">
    <div class="flyer__texture" role="img" aria-label="Blaue Grunge-Struktur an den Rändern"></div>

    <section class="badge">
      <svg viewBox="0 0 360 360" aria-hidden="true">
        <circle cx="180" cy="180" r="158" fill="var(--card)"/>
        <circle cx="180" cy="180" r="158" fill="none" stroke="var(--card)" stroke-width="30" stroke-linecap="round" stroke-dasharray="0 33.09"/>
      </svg>
      <div class="badge__content">
        <h1 class="badge__title">KINDERTRAINING</h1>
        <p class="badge__body">
          Sie erinnern sich. Der Blindtext-Fall im vorigen Jahr. Nun will Karl noch nach Canossa. Und Claudia heiratet zur Busse Copperfield. Jeden Morgen entzünden sie eine Kerze. Jeden Nachmittag ist eine Runde Rosenkranz fällig. Zur Heiligen Marie. Weil Karl mit dem Zopf der Claudia mit dem Smile optisch nette Koran-Typo aufs Mieder hat sticken lassen. Heiliger Blindtext am Busen.
        </p>
        <p class="badge__dates">
          <span class="date--wed">MI, 16.3.2016, 17:00 UHR</span><br>
          <span class="date--thu">DO, 17.3.2016, 17:00 UHR</span><br>
          <span class="date--fri">FR, 18.3.2016, 17:00 UHR</span>
        </p>
        <div class="badge__club">
          <span class="badge__club-dot"></span>
          <span>TSV Blinkau</span>
        </div>
      </div>
    </section>

    <div class="paddles" role="img" aria-label="Illustration: zwei rote Tischtennisschläger mit Ball"></div>

    <p class="flyer__url">WWW.PINGKIDS-BLINKAU.DE</p>
  </main>
</body>
</html>
```